Webdesign Metall- und Stahlbau Harkenfeld GmbH
Zielgruppe
Metall- und Stahlbau Harkenfeld GmbH
Zielgruppe: öffentlicher Bereich, Industrie, Gesundheitswesen > deutschlandweit tätig
Aufgabenstellung
keine bewegten Bilder oder Elemente in der Website
klassisches Layout
sehr konservativ

```html
<!DOCTYPE html>
<html lang="de">
<head>
<meta charset="utf-8">
<title>Metall- und Stahlbau Harkenfeld GmbH</title>
<link href="https://fonts.googleapis.com/css2?family=Arimo:wght@400;500;700&display=swap" rel="stylesheet">
<style>
:root{
  --yellow:#ffcc33;
  --blue:#0d0dc4;
  --blue-btn:#0a0ad0;
  --ink:#1f1f1f;
  --grey:#ececec;
  --grey-footer:#e4e4e4;
  --dark:#2a2a2a;
  --white:#ffffff;
}
*{box-sizing:border-box;margin:0;padding:0}
html,body{width:1200px;height:2652px;overflow:hidden}
body{font-family:"Arimo",Helvetica,Arial,sans-serif;color:var(--ink);background:var(--white);position:relative}
.abs{position:absolute}
.btn-outline{display:inline-block;border:1px solid var(--blue);color:var(--blue);background:transparent;font-size:15px;letter-spacing:.3px;padding:10px 16px;text-decoration:none}
.icon{width:13px;height:13px;vertical-align:-2px;margin-right:5px}

/* top bar */
.topbar{top:0;left:0;width:1200px;height:22px;background:var(--yellow);display:flex;justify-content:flex-end;align-items:center;gap:30px;padding-right:50px;font-size:12px;font-weight:700;color:var(--blue)}

/* header */
.header{top:22px;left:0;width:1200px;height:84px;background:var(--grey);border-bottom:1px solid #d6d6d6}
.brand{position:absolute;left:50px;top:15px;display:flex;align-items:center;gap:12px}
.brand-square{width:54px;height:54px;background:var(--blue)}
.brand-name{font-size:16px;font-weight:700;color:var(--blue);line-height:19px}
.nav{position:absolute;right:50px;top:32px;display:flex;gap:33px;font-size:15px;color:var(--ink)}
.nav a{color:inherit;text-decoration:none}
.nav a.active{color:var(--blue);font-weight:700;text-decoration:underline;text-underline-offset:3px}

/* hero */
.hero{top:106px;left:0;width:1200px;height:567px;background:linear-gradient(100deg,#2d3f5c 0%,#23344f 30%,#111a2a 55%,#050608 75%,#000 100%)}
.hero-text{position:absolute;left:628px;top:145px;width:480px;color:var(--white)}
.hero h1{font-size:44px;line-height:49px;font-weight:700}
.hero p{font-size:17px;line-height:28px;margin-top:14px;letter-spacing:.2px}
.hero .btn{display:inline-block;margin-top:14px;background:var(--blue-btn);color:var(--white);font-size:15px;padding:11px 16px;letter-spacing:.3px}

/* intro */
.intro{top:673px;left:0;width:1200px;height:417px;background:var(--grey)}
.intro-text{position:absolute;left:143px;top:64px;width:350px}
h2.title{font-size:28px;line-height:33px;font-weight:700;color:var(--blue)}
.body-text{font-size:14px;line-height:20px;color:var(--blue);margin-top:16px}
.intro .btn-outline{margin-top:13px}
.intro-photo{position:absolute;left:608px;top:64px;width:448px;height:289px;background:linear-gradient(160deg,#c9cdd2 0%,#8d96a4 45%,#2c3b5c 75%,#3a4656 100%)}

/* competence */
.competence-head{top:1152px;left:0;width:1200px;text-align:center}
.competence-head p{font-size:14px;color:var(--blue);margin-top:12px}
.card{top:1251px;width:355px;height:427px;background:var(--grey);text-align:center}
.card-photo{position:absolute;left:16px;top:33px;width:321px;height:180px}
.card h3{position:absolute;left:0;top:226px;width:100%;font-size:25px;font-weight:700;color:var(--blue)}
.card p{position:absolute;left:20px;top:266px;width:315px;font-size:14px;line-height:20px;color:var(--blue)}
.card .btn-outline{position:absolute;top:354px;left:50%;transform:translateX(-50%);white-space:nowrap}

/* region */
.region-photo{top:1782px;left:175px;width:447px;height:289px;background:linear-gradient(90deg,#dfe5ec 0%,#b9bcbf 35%,#9fa2a4 60%,#c7c8c9 100%)}
.region-text{top:1784px;left:670px;width:360px}
.region-text .btn-outline{margin-top:13px}

/* footer */
.footer{top:2166px;left:0;width:1200px;height:419px;background:var(--grey-footer)}
.footer-brand{position:absolute;left:143px;top:100px;display:flex;gap:12px}
.footer-square{width:54px;height:54px;background:var(--blue)}
.footer-info{color:var(--blue)}
.footer-name{font-size:16px;font-weight:700;line-height:19px}
.footer-tag{font-size:10px;line-height:14px;margin-top:10px}
.footer-addr{font-size:12px;font-weight:700;line-height:20px;margin-top:14px}
.footer-contact{font-size:12px;font-weight:700;line-height:20px;margin-top:6px}
.map{position:absolute;left:498px;top:64px;width:559px;height:290px;background:linear-gradient(135deg,#f6f6f6,#ececec)}

/* bottom */
.bottombar{top:2585px;left:0;width:1200px;height:60px;background:var(--dark);color:var(--white);font-size:14px;display:flex;align-items:center;justify-content:space-between;padding:0 50px}
.legal{display:flex;gap:34px}
.strip{top:2645px;left:0;width:1200px;height:7px;background:var(--yellow)}
</style>
</head>
<body>

<div class="abs topbar">
  <span><svg class="icon" viewBox="0 0 24 24" fill="none" stroke="currentColor" stroke-width="2"><path d="M22 16.9v3a2 2 0 0 1-2.2 2 19.8 19.8 0 0 1-8.6-3.1 19.5 19.5 0 0 1-6-6A19.8 19.8 0 0 1 2.1 4.2 2 2 0 0 1 4.1 2h3a2 2 0 0 1 2 1.7c.1 1 .4 1.9.7 2.8a2 2 0 0 1-.5 2.1L8 9.9a16 16 0 0 0 6 6l1.3-1.3a2 2 0 0 1 2.1-.4c.9.3 1.8.6 2.8.7a2 2 0 0 1 1.7 2z"/></svg>Tel 037521 4830</span>
  <span><svg class="icon" viewBox="0 0 24 24" fill="none" stroke="currentColor" stroke-width="2"><path d="M6 9V2h12v7"/><rect x="2" y="9" width="20" height="9" rx="2"/><path d="M6 14h12v8H6z"/></svg>Fax 037521 4839</span>
  <span><svg class="icon" viewBox="0 0 24 24" fill="none" stroke="currentColor" stroke-width="2"><rect x="2" y="4" width="20" height="16" rx="2"/><path d="M2 6l10 7 10-7"/></svg>info@harkenfeld-stahlbau.de</span>
</div>

<header class="abs header">
  <div class="brand">
    <div class="brand-square"></div>
    <div class="brand-name">Metall- und Stahlbau<br>Harkenfeld GmbH</div>
  </div>
  <nav class="nav">
    <a class="active" href="#">Home</a>
    <a href="#">Leistungen</a>
    <a href="#">Referenzen</a>
    <a href="#">Stellenangebote</a>
    <a href="#">Aktuelles</a>
    <a href="#">Downloads</a>
    <a href="#">Unternehmen</a>
  </nav>
</header>

<section class="abs hero" role="img" aria-label="Schweißer bei der Arbeit in der Werkhalle mit Funkenflug">
  <div class="hero-text">
    <h1>Präzision in Stahl und Metall – seit über 50 Jahren.</h1>
    <p>Seit 1965 verbinden wir sächsische Handwerkstradition mit modernster Technik – vom individuellen Stahlbau bis zum internationalen Strahlenschutz.</p>
    <span class="btn">Zu unseren Leistungen</span>
  </div>
</section>

<section class="abs intro">
  <div class="intro-text">
    <h2 class="title">Verlässlichkeit in zweiter Generation.</h2>
    <p class="body-text">Was 1965 als Bauschlosserei von Reinhard Harkenfeld begann, wird heute von den Söhnen Matthias und Holger Harkenfeld als modernes Industrieunternehmen geführt. Beide Geschäftsführer sind Metallbaumeister aus Überzeugung. In unserer 2010 erweiterten Produktionshalle mit eigener Kranbahn verbinden wir sächsische Handwerkstradition mit technischer Expertise für anspruchsvolle Großprojekte.</p>
    <span class="btn-outline">Persönliches Gespräch vereinbaren</span>
  </div>
  <div class="intro-photo" role="img" aria-label="Die beiden Geschäftsführer in Arbeitskleidung in der Produktionshalle"></div>
</section>

<div class="abs competence-head">
  <h2 class="title">Kompetenz in Stahl und Metall</h2>
  <p>Individuelle Lösungen für Industrie, Medizin und Bauwesen.</p>
</div>

<article class="abs card" style="left:52px">
  <div class="card-photo" role="img" aria-label="Helle Produktionshalle mit gelbem Hallenkran und Stahlträgern" style="background:linear-gradient(180deg,#c9a43a 0%,#e6e6e6 30%,#c8cdd3 70%,#6e747c 100%)"></div>
  <h3>Stahl- &amp; Hallenbau</h3>
  <p>Wir planen, fertigen und montieren tragende Stahlkonstruktionen für Gewerbe und Industrie. Statisch optimiert und termingerecht.</p>
  <span class="btn-outline">Projekt anfragen</span>
</article>

<article class="abs card" style="left:423px">
  <div class="card-photo" role="img" aria-label="Strahlenschutztür aus Edelstahl in einem Betonraum" style="background:linear-gradient(90deg,#bfbfbf 0%,#e9e9e9 35%,#a8aaab 65%,#cfcfcf 100%)"></div>
  <h3>Strahlenschutzbau</h3>
  <p>Unsere Spezialkompetenz für Medizin und Forschung. Wir fertigen hochkomplexe Abschirmungen und Tore weltweit –<br>von Europa bis Asien.</p>
  <span class="btn-outline">Beratung anfordern</span>
</article>

<article class="abs card" style="left:793px">
  <div class="card-photo" role="img" aria-label="Edelstahlgeländer einer Treppe wird mit dem Winkelschleifer bearbeitet" style="background:linear-gradient(120deg,#d8dadc 0%,#aeb2b6 45%,#8a8f94 70%,#50555c 100%)"></div>
  <h3>Sonderkonstruktionen</h3>
  <p>Individuelle Anfertigungen für öffentliche Bauten und Privatkunden. Treppenanlagen, Geländer und Bauteile nach Maß.</p>
  <span class="btn-outline">Angebot einholen</span>
</article>

<div class="abs region-photo" role="img" aria-label="Geöffnete Strahlenschutzschiebetür vor einem Bestrahlungsraum"></div>
<div class="abs region-text">
  <h2 class="title">Unser Einsatzgebiet:<br>Von Sachsen in die Welt.</h2>
  <p class="body-text">Staatshochbauämter, Industrie und Forschungs­einrichtungen vertrauen auf unsere Qualität. Wir sind bundesweit sowie in Österreich und der Schweiz tätig.</p>
  <span class="btn-outline">Referenzliste anfordern</span>
</div>

<footer class="abs footer">
  <div class="footer-brand">
    <div class="footer-square"></div>
    <div class="footer-info">
      <div class="footer-name">Metall- und Stahlbau<br>Harkenfeld GmbH</div>
      <div class="footer-tag">Ihr Familienunternehmen für Präzision<br>aus dem Erzgebirge. Seit 1965.</div>
      <div class="footer-addr">Lindenweg 4<br>09471 Talheim</div>
      <div class="footer-contact">
        <div><svg class="icon" viewBox="0 0 24 24" fill="none" stroke="currentColor" stroke-width="2"><path d="M22 16.9v3a2 2 0 0 1-2.2 2 19.8 19.8 0 0 1-8.6-3.1 19.5 19.5 0 0 1-6-6A19.8 19.8 0 0 1 2.1 4.2 2 2 0 0 1 4.1 2h3a2 2 0 0 1 2 1.7c.1 1 .4 1.9.7 2.8a2 2 0 0 1-.5 2.1L8 9.9a16 16 0 0 0 6 6l1.3-1.3a2 2 0 0 1 2.1-.4c.9.3 1.8.6 2.8.7a2 2 0 0 1 1.7 2z"/></svg>Tel 037521 4830</div>
        <div><svg class="icon" viewBox="0 0 24 24" fill="none" stroke="currentColor" stroke-width="2"><path d="M6 9V2h12v7"/><rect x="2" y="9" width="20" height="9" rx="2"/><path d="M6 14h12v8H6z"/></svg>Fax 037521 4839</div>
        <div><svg class="icon" viewBox="0 0 24 24" fill="none" stroke="currentColor" stroke-width="2"><rect x="2" y="4" width="20" height="16" rx="2"/><path d="M2 6l10 7 10-7"/></svg>info@harkenfeld-stahlbau.de</div>
      </div>
    </div>
  </div>
  <div class="map" role="img" aria-label="Stadtplan mit Standortmarkierung des Firmensitzes"></div>
</footer>

<div class="abs bottombar">
  <span>© 2026 Metall- und Stahlbau Harkenfeld GmbH. Alle Rechte vorbehalten.</span>
  <div class="legal">
    <span>Impressum</span>
    <span>Datenschutzerklärung</span>
    <span>Barrierefreiheit (BFSG)</span>
    <span>AGB</span>
  </div>
</div>
<div class="abs strip"></div>

</body>
</html>
```